Fast Growing Personal Injury Law Firm Needs Business Card Design

We need a business card design for a fast growing personal injury law firm in Florida. Our name is Darren Kolvisty, P.A. Our practice is comprised of younger attorneys (in their 30s) that employ more modern techniques/tools than our older competition. We would prefer a look that is a modern play on a classic look. Also, we would like to continue using a color scheme that employs navy blue and kelly green (other shades of green could be fine too) as well as our "E" logo.

Industry/Entity Type

Law Firm

```html
<!DOCTYPE html>
<html lang="en">
<head>
<meta charset="utf-8">
<title>Darren Kolvisty, P.A. — Business Card</title>
<link rel="stylesheet" href="https://fonts.googleapis.com/css2?family=Cinzel:wght@500;600&family=Lato:wght@400&display=swap">
<style>
  :root {
    --navy: #0b2a5c;
    --green: #07853f;
    --ink: #333a44;
    --paper: #ffffff;
    --backdrop: #5a5a5a;
    --rule: #9aa3ad;
  }
  * { margin: 0; padding: 0; box-sizing: border-box; }
  html, body { width: 1200px; height: 820px; overflow: hidden; }
  body {
    position: relative;
    background: var(--backdrop);
    font-family: "Lato", Arial, sans-serif;
  }
  .card {
    position: absolute;
    top: 257px;
    width: 477px;
    height: 274px;
    overflow: hidden;
  }
  .card--front { left: 115px; background: var(--paper); }
  .card--back { left: 620px; background: var(--navy); }

  /* front: firm name block */
  .brand-square {
    position: absolute; left: 52px; top: 43px;
    width: 71px; height: 62px;
    background: var(--navy);
  }
  .firm-name {
    position: absolute; left: 135px; top: 47px;
    font-family: "Cinzel", Georgia, serif; font-weight: 600;
    font-size: 21px; color: var(--navy); letter-spacing: 0.5px;
    white-space: nowrap;
  }
  .firm-rule {
    position: absolute; left: 135px; top: 76px; width: 265px; height: 1px;
    background: var(--navy);
  }
  .firm-tagline {
    position: absolute; left: 135px; top: 79px;
    font-family: "Cinzel", Georgia, serif; font-weight: 600;
    font-size: 14px; color: var(--green); letter-spacing: 1.6px;
    white-space: nowrap;
  }

  /* front: person */
  .person { position: absolute; left: 50px; top: 146px; }
  .person__name { font-size: 17px; color: var(--navy); line-height: 22px; }
  .person__title {
    font-size: 13px; color: var(--ink); line-height: 18px;
    width: 183px; border-bottom: 1px solid var(--navy); padding-bottom: 2px;
  }
  .person__address { margin-top: 4px; font-size: 13px; color: var(--ink); line-height: 16px; }

  .divider {
    position: absolute; left: 255px; top: 150px; width: 1px; height: 74px;
    background: var(--rule);
  }

  .contacts { position: absolute; left: 281px; top: 147px; list-style: none; }
  .contacts li {
    display: flex; align-items: center; gap: 4px;
    font-size: 13px; color: var(--ink); line-height: 20px;
  }
  .contacts svg { width: 11px; height: 11px; flex: none; }

  .front-band { position: absolute; left: 0; bottom: 0; width: 477px; height: 18px; }

  /* back */
  .back-field { position: absolute; left: 0; top: 0; width: 190px; height: 274px; background: var(--green); }
  .back-text {
    position: absolute; right: 16px; top: 212px; text-align: right;
    font-family: "Cinzel", Georgia, serif; font-weight: 600; color: var(--paper);
  }
  .back-text__name { font-size: 17px; letter-spacing: 0.4px; line-height: 20px; }
  .back-text__tagline {
    font-size: 11.5px; letter-spacing: 1.4px; line-height: 15px;
    border-top: 1px solid var(--paper); padding-top: 1px;
  }
  .back-text__url { margin-top: 5px; font-size: 10px; letter-spacing: 2.6px; font-weight: 500; }
</style>
</head>
<body>

<section class="card card--front" aria-label="Business card front">
  <div class="brand-square"></div>
  <div class="firm-name">Darren Kolvisty, P.A.</div>
  <div class="firm-rule"></div>
  <div class="firm-tagline">Personal Injury Attorneys</div>

  <div class="person">
    <p class="person__name">Darren Kolvisty</p>
    <p class="person__title">Attorney at Law</p>
    <p class="person__address">2150 Harbor Point Drive Suite 300<br>Bayside Park, Florida 34000</p>
  </div>

  <div class="divider"></div>

  <ul class="contacts">
    <li>
      <svg viewBox="0 0 12 12"><circle cx="6" cy="6" r="6" fill="var(--navy)"/><path d="M3.6 3.2l1.2-.2.7 1.6-.8.6c.4.9 1 1.5 1.9 1.9l.6-.8 1.6.7-.2 1.2C6 8.4 3.4 5.8 3.6 3.2z" fill="#fff"/></svg>
      941.555.0182
    </li>
    <li>
      <svg viewBox="0 0 12 12"><circle cx="6" cy="6" r="6" fill="var(--navy)"/><rect x="4" y="2.6" width="4" height="6.8" rx=".6" fill="#fff"/><rect x="4.7" y="3.4" width="2.6" height="4.2" fill="var(--navy)"/></svg>
      941.555.0147
    </li>
    <li>
      <svg viewBox="0 0 12 12"><circle cx="6" cy="6" r="6" fill="var(--navy)"/><rect x="3" y="4" width="6" height="4.2" fill="#fff"/><path d="M3 4l3 2.3L9 4" fill="none" stroke="var(--navy)" stroke-width=".7"/></svg>
      darren@kolvistylaw.com
    </li>
    <li>
      <svg viewBox="0 0 12 12"><circle cx="6" cy="6" r="6" fill="var(--navy)"/><circle cx="6" cy="6" r="3.3" fill="none" stroke="#fff" stroke-width=".8"/><path d="M2.7 6h6.6M6 2.7c-1.6 2-1.6 4.6 0 6.6M6 2.7c1.6 2 1.6 4.6 0 6.6" fill="none" stroke="#fff" stroke-width=".6"/></svg>
      www.kolvistylaw.com
    </li>
  </ul>

  <svg class="front-band" viewBox="0 0 477 18" preserveAspectRatio="none" aria-hidden="true">
    <polygon points="0,0 252,0 245,11 0,11" fill="var(--green)"/>
    <polygon points="257,0 477,0 477,18 0,18 0,14 248,14" fill="var(--navy)"/>
  </svg>
</section>

<section class="card card--back" aria-label="Business card back">
  <div class="back-field"></div>
  <div class="back-text">
    <p class="back-text__name">Darren Kolvisty, P.A.</p>
    <p class="back-text__tagline">Personal Injury Attorneys</p>
    <p class="back-text__url">www.kolvistylaw.com</p>
  </div>
</section>

</body>
</html>
```